Powerpoint template design for Oil and Gas Investment Fund Pitchdeck

I need a template design for an oil and gas investment fund pitch deck. Design needs to be clean and have plenty of space for inserting graphics. Audience is high net worth individuals and corporate finance executives (private equity firms). We will need a title page with our logo and some oil& gas images (some included already) and the template for the internal pages. A rough example is attached. I would like to keep the current page dimensions because we have many financial charts we will want to add to the template pages. So the template will need to include title page, internal page, and a team page.

Target Market(s)

High etw worth individual investors and corporate finance professionals

Industry/Entity Type

Oil an dgas investment fund

Font styles to use
Serif

Requirements
Must have
• title page, interior page, team page

```html
<!DOCTYPE html>
<html lang="en">
<head>
<meta charset="utf-8">
<title>Halvard Energy Partners – Pitch Deck Template</title>
<link rel="stylesheet" href="https://fonts.googleapis.com/css2?family=Arimo:wght@400;700&family=Libre+Baskerville:wght@400;700&display=swap">
<style>
:root{
  --page:#f3f4f6;
  --slide:#ffffff;
  --ink:#1b1b1b;
  --muted:#6f6f6f;
  --navy:#1f2450;
  --navy-deep:#12152e;
  --accent:#e06a00;
  --arrow:#e21b1b;
  --green:#2a9a3a;
  --night:#0d1014;
  --shadow:0 1px 4px rgba(0,0,0,.18);
}
*{box-sizing:border-box;margin:0;padding:0}
html,body{width:1200px;height:4208px;overflow:hidden;background:var(--page)}
body{position:relative;font-family:Arimo,Arial,sans-serif;color:var(--ink)}
.slide{position:absolute;left:51px;width:1097px;height:619px;background:var(--slide);box-shadow:var(--shadow);overflow:hidden}
.slide-title-page{top:70px}
.slide-industry{top:767px}
.slide-opportunity{top:1448px}
.slide-team{top:2126px}
.slide-disclaimer{top:2805px}
.slide-closing{top:3493px}

/* shared interior chrome */
.header-rule{position:absolute;left:16px;top:29px;width:42px;height:2px;background:var(--ink)}
.slide-heading{position:absolute;left:16px;top:42px;font-size:26px;font-weight:400;letter-spacing:.2px}
.slide-subheading{position:absolute;left:16px;top:78px;font-size:12px;color:#444;letter-spacing:.3px}
.corner-brand{position:absolute;right:16px;top:28px;text-align:center;font-family:"Libre Baskerville",Georgia,serif;color:var(--ink)}
.corner-brand .name{font-size:12px;font-weight:700;letter-spacing:1.5px;display:block}
.corner-brand .sub{font-size:6px;letter-spacing:2.4px;display:block;margin-top:1px}
.footer-copy{position:absolute;left:16px;top:584px;font-size:11px;color:#333}
.footer-page{position:absolute;right:16px;top:584px;font-size:11px;color:#333}

/* title page */
.hero-photo{position:absolute;inset:0;background:
  radial-gradient(ellipse at 75% 40%,rgba(90,95,140,.55),transparent 60%),
  linear-gradient(180deg,#2c3160 0%,var(--navy) 45%,var(--navy-deep) 100%)}
.hero-brand{position:absolute;left:0;width:552px;top:205px;text-align:center;color:#fff;font-family:"Libre Baskerville",Georgia,serif}
.hero-mark{width:40px;height:40px;border:3px solid #fff;margin:0 auto 22px}
.hero-brand .name{font-size:38px;letter-spacing:7px;line-height:1}
.hero-brand .sub{font-size:14px;letter-spacing:9px;margin-top:6px}
.hero-tagline{position:absolute;left:0;width:552px;top:348px;text-align:center;color:#fff;font-family:"Libre Baskerville",Georgia,serif;font-weight:700;font-size:18px;line-height:40px}

/* industry */
.dot-texture{position:absolute;left:0;right:0;top:100px;bottom:40px;background:radial-gradient(circle,#e9ebee 1px,transparent 1.4px) 0 0/9px 9px;opacity:.5}
.icon-row{position:absolute;left:64px}
.row-major{top:184px}
.row-divest{top:370px}
.industry-note{position:absolute;left:624px;width:420px;font-size:16px;line-height:28px;color:#333}
.note-major{top:188px}
.note-divest{top:386px}
.industry-note .hl{color:var(--accent)}

/* opportunity */
.faint-brand{position:absolute;left:0;right:0;top:250px;text-align:center;font-family:"Libre Baskerville",Georgia,serif;font-size:70px;letter-spacing:10px;color:#f1f2f4}

/* team */
.team-grid{position:absolute;left:0;top:111px;width:1097px}
.member{position:absolute;width:230px;text-align:center;transform:translateX(-50%)}
.member:nth-child(1){left:150px}.member:nth-child(2){left:416px}.member:nth-child(3){left:683px}.member:nth-child(4){left:947px}
.portrait{width:150px;height:150px;border-radius:50%;margin:0 auto}
.member h3{margin-top:23px;font-size:15px;font-weight:700;letter-spacing:.3px}
.member .role{margin-top:6px;font-size:13px;line-height:20px;color:var(--muted)}
.member .bio{margin-top:10px;font-size:9.5px;line-height:20px;color:#555}
.partners{position:absolute;left:50px;right:50px;top:496px;display:flex;justify-content:space-between;align-items:center}
.partner{font-size:16px;font-weight:700;color:#2d3a6b;display:flex;align-items:center;gap:6px}
.partner .dot{width:14px;height:14px;background:#2d3a6b}

/* disclaimer */
.disclaimer{position:absolute;left:72px;top:166px;width:480px;font-size:15px;line-height:28px;color:#333}
.feature-photo{position:absolute;left:553px;top:93px;width:503px;height:403px;background:linear-gradient(180deg,#c4553a 0%,#e08a45 45%,#3b2a22 70%,#1d1a1f 100%)}

/* closing */
.closing-photo{position:absolute;inset:0;background:linear-gradient(180deg,#171b21,var(--night))}
.closing-brand{position:absolute;left:0;right:0;top:180px;text-align:center;color:#fff;font-family:"Libre Baskerville",Georgia,serif}
.closing-brand .name{font-size:36px;letter-spacing:7px}
.closing-brand .sub{font-size:13px;letter-spacing:9px;margin-top:6px}
.thank-you{position:absolute;left:0;right:0;top:360px;text-align:center;color:#fff;font-family:Arimo,Arial,sans-serif;font-weight:700;font-size:100px;letter-spacing:1px;line-height:1}
</style>
</head>
<body>

<section class="slide slide-title-page">
  <div class="hero-photo" role="img" aria-label="Offshore oil platform at dusk under a navy sky"></div>
  <div class="hero-brand">
    <div class="hero-mark"></div>
    <div class="name">HALVARD</div>
    <div class="sub">ENERGY PARTNERS</div>
  </div>
  <p class="hero-tagline">CONSOLIDATING PROFITABLE CONVENTIONAL<br>WEST TEXAS OIL &amp; GAS &nbsp;WELLS INTO A HIGH<br>RETURN &nbsp;INVESTMENT FUND</p>
</section>

<section class="slide slide-industry">
  <div class="dot-texture"></div>
  <div class="header-rule"></div>
  <h2 class="slide-heading">THE INDUSTRY TODAY</h2>
  <p class="slide-subheading">SUBTITLE GOES HERE</p>
  <div class="corner-brand"><span class="name">HALVARD</span><span class="sub">ENERGY PARTNERS</span></div>

  <svg class="icon-row row-major" width="520" height="90" viewBox="0 0 520 90">
    <g fill="none" stroke="#111" stroke-width="4">
      <g id="derrick"><path d="M10 85 L25 10 L40 85 M14 65 H36 M18 45 H32 M21 28 H29 M14 65 L32 45 M36 65 L18 45"/><path d="M19 10 H31" stroke-width="6"/><path d="M4 86 H46" stroke-width="5"/></g>
      <use href="#derrick" x="68"/><use href="#derrick" x="136"/>
    </g>
    <path d="M227 37 H245 V30 L258 40 L245 50 V43 H227Z" fill="var(--arrow)"/>
    <g fill="#111" stroke="#fff" stroke-width="3">
      <g id="barrel"><rect x="294" y="8" width="62" height="76" rx="10"/><ellipse cx="325" cy="14" rx="29" ry="9"/><path d="M296 40 Q325 50 354 40 M296 62 Q325 72 354 62" fill="none"/></g>
      <use href="#barrel" x="70"/><use href="#barrel" x="140"/>
    </g>
  </svg>
  <p class="industry-note note-major">Typical “Major” <span class="hl">O&amp;G</span> Companies have thousands of horizontal wells and thousands of vertical wells. They want to focus on horizontal.</p>

  <svg class="icon-row row-divest" width="520" height="115" viewBox="0 0 520 115">
    <ellipse cx="92" cy="57" rx="90" ry="52" fill="none" stroke="var(--green)" stroke-width="3.5" stroke-dasharray="10 7"/>
    <g fill="none" stroke="#111" stroke-width="2">
      <g id="mini"><path d="M50 45 L56 22 L62 45 M52 37 H60 M48 46 H64"/></g>
      <use href="#mini" x="20"/><use href="#mini" x="40"/><use href="#mini" x="60"/><use href="#mini" x="80"/>
      <use href="#mini" y="32"/><use href="#mini" x="20" y="32"/><use href="#mini" x="40" y="32"/><use href="#mini" x="60" y="32"/><use href="#mini" x="80" y="32"/>
    </g>
    <path d="M227 57 H245 V50 L258 60 L245 70 V63 H227Z" fill="var(--arrow)"/>
    <g fill="#111" stroke="#fff" stroke-width="2">
      <g id="small-barrel"><rect x="300" y="6" width="32" height="44" rx="6"/><ellipse cx="316" cy="10" rx="14" ry="5"/><path d="M301 28 Q316 33 331 28" fill="none"/></g>
      <use href="#small-barrel" x="56"/><use href="#small-barrel" x="112"/><use href="#small-barrel" x="168"/>
      <use href="#small-barrel" y="54"/><use href="#small-barrel" x="56" y="54"/><use href="#small-barrel" x="112" y="54"/><use href="#small-barrel" x="168" y="54"/>
    </g>
  </svg>
  <p class="industry-note note-divest">Strong economic motivation to divest Vertical wells on good terms to trusted operators like Halvard/HCP.</p>

  <p class="footer-copy">© Copyright 2022 Halvard.All Rights Reserved.</p>
  <p class="footer-page">Page 02</p>
</section>

<section class="slide slide-opportunity">
  <div class="faint-brand">HALVARD</div>
  <div class="header-rule"></div>
  <h2 class="slide-heading">THE OPPORTUNITY</h2>
  <p class="slide-subheading">INTERNAL TEMPLATE PAGE EXAMPLE</p>
  <div class="corner-brand"><span class="name">HALVARD</span><span class="sub">ENERGY PARTNERS</span></div>
  <p class="footer-copy">© Copyright 2022 Halvard.All Rights Reserved.</p>
  <p class="footer-page">Page 03</p>
</section>

<section class="slide slide-team">
  <div class="header-rule"></div>
  <h2 class="slide-heading">TEAM</h2>
  <p class="slide-subheading">SUBTITLE GOES HERE</p>
  <div class="corner-brand"><span class="name">HALVARD</span><span class="sub">ENERGY PARTNERS</span></div>
  <div class="team-grid">
    <article class="member">
      <div class="portrait" role="img" aria-label="Portrait of Daniel Whitcomb" style="background:linear-gradient(160deg,#8a8f96,#2b2e35)"></div>
      <h3>DANIEL WHITCOMB</h3>
      <p class="role">Managing Partner + CEO HCP<br>Resources</p>
      <p class="bio">Numerous oilfield operations leadership posit<br>ions including VP &amp; GM for Redmesa where he<br>was responsible for 1000+ horizontal wells and<br>6000+ vertical wells</p>
    </article>
    <article class="member">
      <div class="portrait" role="img" aria-label="Portrait of Marcus Ellery" style="background:linear-gradient(160deg,#5a5a5c,#b08a70)"></div>
      <h3>MARCUS ELLERY</h3>
      <p class="role">Managing Partner,<br>Halvard</p>
      <p class="bio">Extensive P&amp;L and management experience,<br>including positions at Kessel Mining &amp;<br>Metals, a Global 50 electronic materials<br>company.</p>
    </article>
    <article class="member">
      <div class="portrait" role="img" aria-label="Portrait of Wade Tillman at an oilfield site" style="background:linear-gradient(160deg,#9aa3ad,#6b5a4c)"></div>
      <h3>WADE TILLMAN</h3>
      <p class="role">Operations Manager</p>
      <p class="bio">Over 40 years of experience in oilfield<br>operations, drilling, and equipment mainten<br>ance. Wade manages our daily field operations<br>and production efforts.</p>
    </article>
    <article class="member">
      <div class="portrait" role="img" aria-label="Portrait of Laura Prescott" style="background:linear-gradient(160deg,#7c7068,#3d2e28)"></div>
      <h3>LAURA PRESCOTT</h3>
      <p class="role">Reserves Analysis and Property<br>Evaluation.</p>
      <p class="bio">Registered Petroleum Engineer with 30+ years<br>experience and significant background in the<br>Permian Basin</p>
    </article>
  </div>
  <div class="partners">
    <span class="partner"><span class="dot"></span>CARROW VANCE</span>
    <span class="partner">Brandt, Hollis &amp; Weaver</span>
    <span class="partner">Plains Federal Bank</span>
    <span class="partner">STONEFIELD PETROLEUM</span>
    <span class="partner">Kestrel Labs</span>
  </div>
  <p class="footer-copy">© Copyright 2022 Halvard.All Rights Reserved.</p>
  <p class="footer-page">Page 04</p>
</section>

<section class="slide slide-disclaimer">
  <div class="header-rule"></div>
  <h2 class="slide-heading">YOUR TITLE HERE</h2>
  <p class="slide-subheading">SUBTITLE GOES HERE</p>
  <div class="corner-brand"><span class="name">HALVARD</span><span class="sub">ENERGY PARTNERS</span></div>
  <p class="disclaimer">Nothing contained in these documents and materials is meant to be, and shall not be considered, a security offering, an offer to invest, or a solicitation of funds for any purpose. &nbsp;All information contained in these materials and documents, including, but not limited to, numbers, dollar amounts, rates of return, oil production, projections, etc. are included in such materials and documents purely for informational and discussion purposes only, and are strictly conjecture. &nbsp;The success of this prop osed business idea or venture is not guaranteed in any way, and any investment in such business idea or venture carries the risk of signific ant or complete loss of investment.</p>
  <div class="feature-photo" role="img" aria-label="Oil platform silhouetted against an orange sunset over the sea"></div>
  <p class="footer-copy">© Copyright 2022 Halvard.All Rights Reserved.</p>
  <p class="footer-page">Page 05</p>
</section>

<section class="slide slide-closing">
  <div class="closing-photo" role="img" aria-label="Dark night photo of an oil platform"></div>
  <div class="closing-brand">
    <div class="name">HALVARD</div>
    <div class="sub">ENERGY PARTNERS</div>
  </div>
  <h2 class="thank-you">THANK YOU</h2>
</section>

</body>
</html>
```